Flyer Design for new yoga and pilates studio for Health care centre

We are a health care company in Sydney CBD, we have chiropractors, podiatry, massage, nutrition, massage etc. but we are now expanding to add Yoga and Pilates to our centre.
We want to make sure the emphasis that that studio will be boutique, never crowded, limited number of participants and run by health professionals. Also that is it located in the Sydney CBD opposite HMK. Our target is more corporate since we are in the City. This flyer will be handed out in the street in the city to inform people of our new studio. The flyer must be A5 and include our logo and our colours which I have attached. Our website is www.brightlanewellness.com.au.
Thank you!

Requirements
Must have
• the flyer must be A5 in size and include our logo, our colours and you can use one or more of the photos provided. I have attached the photos.

```html
<!DOCTYPE html>
<html lang="en">
<head>
<meta charset="utf-8">
<title>Brightlane Wellness – Yoga &amp; Pilates Flyer</title>
<link href="https://fonts.googleapis.com/css2?family=Open+Sans:wght@700;800&family=PT+Sans+Narrow:wght@400;700&display=swap" rel="stylesheet">
<style>
  :root {
    --canvas: #ece9ef;
    --magenta: #c2358f;
    --magenta-deep: #a3287a;
    --pink-light: #ecb6dc;
    --purple: #6b5ba8;
    --purple-deep: #4f4296;
    --lavender: #b9acdc;
    --lavender-pale: #d3cdea;
    --orange: #f18a1c;
    --orange-deep: #e0651a;
    --orange-pale: #fbd9b0;
    --text-light: #ffffff;
    --text-address: #b52d86;
    --text-contact: #c02a88;
  }
  * { margin: 0; padding: 0; box-sizing: border-box; }
  html, body { width: 1200px; height: 1200px; overflow: hidden; background: var(--canvas); }
  .flyer {
    position: absolute; left: 200px; top: 45px;
    width: 800px; height: 1110px; overflow: hidden;
    background: #fff;
    box-shadow: 0 6px 24px rgba(40, 20, 60, .18);
    font-family: "PT Sans Narrow", "Arial Narrow", sans-serif;
  }
  .flyer-bg { position: absolute; inset: 0; }
  .abs { position: absolute; }

  .brand-name {
    left: 16px; top: 62px;
    font-family: "Open Sans", Arial, sans-serif; font-weight: 800;
    font-size: 26px; color: var(--text-light); letter-spacing: -.3px;
  }
  .tagline {
    left: 318px; top: 68px;
    font-family: "Open Sans", Arial, sans-serif; font-weight: 700;
    font-size: 19px; color: var(--lavender-pale);
  }
  .mission {
    left: 29px; top: 150px; width: 445px;
    font-size: 19.5px; line-height: 1.3; color: var(--text-light);
  }
  .services-title { left: 42px; top: 332px; font-size: 24px; font-weight: 400; color: var(--text-light); }
  .services-list {
    left: 124px; top: 386px; width: 380px;
    list-style: none; display: grid; grid-template-columns: 201px 170px; row-gap: 2px;
  }
  .services-list li {
    font-size: 25px; line-height: 33px; color: var(--magenta-deep);
    display: flex; align-items: center; gap: 18px;
  }
  .services-list li::before {
    content: ""; width: 14px; height: 14px; background: var(--purple); flex: none;
  }
  .selling-points {
    right: 322px; top: 500px; list-style: none; text-align: right;
  }
  .selling-points li { font-size: 27px; line-height: 40px; color: var(--orange-deep); white-space: nowrap; }
  .selling-points strong { font-weight: 700; color: var(--orange); }
  .address {
    left: 382px; top: 720px; font-size: 17px; line-height: 24.5px;
    color: var(--text-address); list-style: none;
  }
  .phone-lines {
    left: 603px; top: 746px; list-style: none;
    font-size: 19px; line-height: 28px; font-weight: 700; color: var(--text-contact);
  }
  .badge-text {
    left: 61px; top: 722px; width: 262px; text-align: center;
    font-family: "Open Sans", Arial, sans-serif; font-weight: 800;
    color: var(--orange-pale);
    -webkit-text-stroke: 3px var(--orange-deep); paint-order: stroke fill;
    line-height: .95; letter-spacing: -1px;
  }
  .badge-text .now { display: block; font-size: 54px; }
  .badge-text .yoga { display: block; font-size: 76px; color: #fff; }
  .badge-text .pilates { display: block; font-size: 52px; color: #fff; }
  .website {
    left: 20px; top: 1070px;
    font-family: "Open Sans", Arial, sans-serif; font-weight: 700; font-size: 18px; color: var(--text-light);
  }
  .email { right: 20px; top: 1070px; font-size: 19px; color: var(--text-light); }
</style>
</head>
<body>
<main class="flyer">
  <svg class="flyer-bg" viewBox="0 0 800 1110" width="800" height="1110" aria-hidden="true">
    <defs>
      <linearGradient id="topPink" x1="0" y1="0" x2="0" y2="1">
        <stop offset="0" stop-color="#d25aa6"/>
        <stop offset="1" stop-color="#e9a6d2"/>
      </linearGradient>
      <linearGradient id="swoosh" x1="0" y1="0" x2="1" y2="0">
        <stop offset="0" stop-color="#c2358f"/>
        <stop offset="1" stop-color="#b9acdc"/>
      </linearGradient>
      <linearGradient id="bottomWave" x1="0" y1="0" x2="0" y2="1">
        <stop offset="0" stop-color="#b9acdc"/>
        <stop offset="1" stop-color="#4f4296"/>
      </linearGradient>
      <linearGradient id="ringPurple" x1="0" y1="0" x2="1" y2="1">
        <stop offset="0" stop-color="#7b6cc0"/>
        <stop offset="1" stop-color="#4f4296"/>
      </linearGradient>
      <linearGradient id="ringMagenta" x1="0" y1="0" x2="1" y2="1">
        <stop offset="0" stop-color="#e05aae"/>
        <stop offset="1" stop-color="#a3287a"/>
      </linearGradient>
      <radialGradient id="badgeFill" cx=".4" cy=".35" r=".7">
        <stop offset="0" stop-color="#fbb94a"/>
        <stop offset="1" stop-color="#e0651a"/>
      </radialGradient>
      <linearGradient id="photoFill" x1="0" y1="0" x2="1" y2="0">
        <stop offset="0" stop-color="#e8d6cf"/>
        <stop offset="1" stop-color="#c2c6de"/>
      </linearGradient>
    </defs>

    <path d="M0 0 H800 V300 C600 270 330 330 0 470 Z" fill="url(#topPink)"/>
    <path d="M0 470 C330 330 600 270 800 300 V330 C600 310 320 380 0 520 Z" fill="url(#swoosh)" opacity=".55"/>
    <path d="M0 380 C250 350 380 380 800 330 V300 C600 270 330 330 0 470 Z" fill="#cf4f9e" opacity=".35"/>

    <rect x="0" y="0" width="800" height="37" fill="var(--pink-light)"/>
    <rect x="0" y="37" width="800" height="64" fill="var(--purple)"/>
    <rect x="0" y="37" width="300" height="64" fill="var(--magenta)"/>

    <g fill="var(--orange)">
      <rect x="0" y="511" width="18" height="18"/>
      <rect x="0" y="551" width="18" height="18"/>
      <rect x="0" y="592" width="18" height="18"/>
      <rect x="0" y="632" width="18" height="18"/>
    </g>
    <g fill="var(--orange)" opacity=".45">
      <rect x="28" y="511" width="18" height="18"/><rect x="56" y="511" width="18" height="18"/>
      <rect x="28" y="551" width="18" height="18"/><rect x="56" y="551" width="18" height="18"/><rect x="84" y="551" width="18" height="18"/>
      <rect x="28" y="592" width="18" height="18"/><rect x="56" y="592" width="18" height="18"/>
      <rect x="28" y="632" width="18" height="18"/><rect x="56" y="632" width="18" height="18"/>
    </g>
    <g fill="var(--orange)" opacity=".18">
      <rect x="84" y="511" width="18" height="18"/><rect x="112" y="551" width="18" height="18"/>
      <rect x="84" y="592" width="18" height="18"/><rect x="112" y="592" width="18" height="18"/>
      <rect x="84" y="632" width="18" height="18"/><rect x="112" y="632" width="18" height="18"/><rect x="140" y="632" width="18" height="18"/>
    </g>

    <path d="M0 900 C260 810 520 800 800 740 V1110 H0 Z" fill="url(#bottomWave)"/>
    <path d="M0 860 C260 790 520 780 800 720 V745 C520 805 260 820 0 905 Z" fill="var(--lavender)" opacity=".5"/>
    <rect x="0" y="1058" width="800" height="52" fill="var(--purple-deep)" opacity=".85"/>

    <circle cx="640" cy="182" r="126" fill="url(#ringPurple)"/>
    <circle cx="640" cy="182" r="109" fill="url(#photoFill)" role="img" aria-label="Photo: woman in an upward-facing dog yoga pose on a mat"/>
    <circle cx="628" cy="543" r="137" fill="url(#ringMagenta)"/>
    <circle cx="628" cy="543" r="118" fill="url(#photoFill)" role="img" aria-label="Photo: businessman meditating cross-legged on a table amid office colleagues"/>

    <path d="M80 1060 C120 960 250 890 420 870 C560 855 680 840 760 835 V1060 Z" fill="url(#photoFill)" role="img" aria-label="Photo: woman and man in cobra pose on yoga mats"/>

    <circle cx="192" cy="819" r="132" fill="url(#badgeFill)"/>
    <circle cx="192" cy="819" r="112" fill="none" stroke="#fff" stroke-width="3" opacity=".6"/>
  </svg>

  <div class="abs brand-name">Brightlane Wellness</div>
  <div class="abs tagline">For complete wellbeing.</div>

  <p class="abs mission">Our Mission is to deliver superior healthcare services, enabling our practice members to achieve the highest health potential. We take an holistic approach to our practice - we believe in healthcare, not sick-care; and that prevention is better than the cure.</p>

  <h2 class="abs services-title">Our Services</h2>
  <ul class="abs services-list">
    <li>Chiropractic</li>
    <li>Massage</li>
    <li>Podiatry</li>
    <li>Acupuncture</li>
  </ul>

  <ul class="abs selling-points">
    <li><strong>Unique</strong> approach to fitness and health</li>
    <li><strong>Limited</strong> number of particpants</li>
    <li>Run by <strong>health professionals</strong></li>
    <li>located in the <strong>Sydney CBD</strong></li>
  </ul>

  <div class="abs badge-text">
    <span class="now">Now</span>
    <span class="yoga">YOGA</span>
    <span class="pilates">&amp;Pilates</span>
  </div>

  <ul class="abs address">
    <li>Brightlane Wellness</li>
    <li>Level 5, Harbour Gate Tower</li>
    <li>48 Carrow St (Opposite the HMK)</li>
    <li>Sydney NSW 2000 Australia</li>
  </ul>
  <ul class="abs phone-lines">
    <li>Tel: (02) 9100 4826</li>
    <li>Fax: (02) 9100 4827</li>
  </ul>

  <div class="abs website">www.brightlanewellness.com.au</div>
  <div class="abs email">Email: frontdesk@brightlanewellness.com.au</div>
</main>
</body>
</html>
```